Bright Mesh Business Card

This is a business card for a printing company but I actually don't have a logo. Just need to typeset the words "Bright Mesh Printing" as the logo. Then add my name "Loretta Vance" + phone number + address

Target Market(s)

ceos and professionals

Industry/Entity Type

printing and manufacturing

Contact Information for Business Card

Bright Mesh Printing/ 4617 calloway st. S. El Monte, CA 91648/ 626-417-3980/ Loretta Vance

Font styles to use
Serif
Other font styles liked:
• a modern font would be nice

Colors
0054AA
0677BA
7BADD7
CADEEF
E8F1F8
0094D4
00A9DD
6FCCEA
C7EBF8
E9F6FB

Requirements
Must have
• company name, number, address
Nice to have
• nice bold feel
Should not have
• nothing in particular

```html
<!DOCTYPE html>
<html lang="en">
<head>
<meta charset="utf-8">
<title>Bright Mesh Printing – Business Card</title>
<link rel="stylesheet" href="https://fonts.googleapis.com/css2?family=Source+Sans+3:wght@400;600&display=swap">
<style>
  :root {
    --brand-blue: #1455a5;
    --brand-cyan: #0ea5da;
    --text-gray: #7a7a7a;
    --card-border: #222222;
    --paper: #ffffff;
  }
  * { margin: 0; padding: 0; box-sizing: border-box; }
  html, body { width: 1200px; height: 1200px; overflow: hidden; background: var(--paper); }
  body { position: relative; font-family: "Source Sans 3", sans-serif; }

  .card {
    position: absolute;
    left: 284px;
    width: 656px;
    height: 412px;
  }
  .card--front { top: 146px; background: var(--brand-blue); }
  .card--back { top: 636px; background: var(--paper); border: 2px solid var(--card-border); }

  .stripe {
    position: absolute;
    left: 0; right: 0;
    height: 7px;
    background: var(--brand-cyan);
  }
  .stripe--top { top: 11px; }
  .stripe--bottom { top: 395px; }

  .company-name {
    position: absolute;
    left: 0; right: 0;
    text-align: center;
    font-family: "Source Sans 3", sans-serif;
    font-weight: 600;
    font-size: 50px;
    line-height: 60px;
  }
  .card--front .company-name { top: 176px; color: var(--paper); }
  .card--back .company-name { top: 116px; color: var(--brand-blue); }

  .contact-name {
    position: absolute;
    left: 0; right: 0;
    top: 256px;
    text-align: center;
    font-size: 33px;
    line-height: 36px;
    color: var(--brand-blue);
  }
  .contact-name__last { color: var(--brand-cyan); }

  .contact-role {
    position: absolute;
    left: 0; right: 0;
    top: 291px;
    text-align: center;
    font-size: 24px;
    line-height: 26px;
    color: var(--text-gray);
  }

  .contact-details {
    position: absolute;
    left: 0; right: 0;
    top: 334px;
    display: flex;
    justify-content: center;
    align-items: center;
    font-size: 17.5px;
    color: var(--text-gray);
  }
  .contact-details__rule {
    width: 2px;
    height: 42px;
    background: var(--text-gray);
    margin: 0 8px;
  }
</style>
</head>
<body>
  <section class="card card--front" aria-label="Card front">
    <div class="stripe stripe--top"></div>
    <p class="company-name">Bright Mesh Printing</p>
    <div class="stripe stripe--bottom"></div>
  </section>

  <section class="card card--back" aria-label="Card back">
    <p class="company-name">Bright Mesh Printing</p>
    <p class="contact-name">Loretta <span class="contact-name__last">Vance</span></p>
    <p class="contact-role">Owner</p>
    <p class="contact-details">
      <span>4617 calloway st. S. El Monte,</span>
      <span class="contact-details__rule"></span>
      <span>CA 91648/ 626-417-3980</span>
    </p>
  </section>
</body>
</html>
```